Mendwell47 Business Card Redesign

I want to create a design for brand new business cards, I need something exceptional for clear plastic business card design. Please do not submit without it being on a clear design. Photos of the various logo versions attached.

```html
<!DOCTYPE html>
<html lang="en">
<head>
<meta charset="utf-8">
<title>Mendwell47 Business Card</title>
<link href="https://fonts.googleapis.com/css2?family=Roboto:wght@400;500;700&display=swap" rel="stylesheet">
<style>
  :root {
    --page: #dfe5ec;
    --frost-top: #f4f6f9;
    --frost-bottom: #e3e8ef;
    --navy: #27345a;
    --navy-deep: #1c2747;
    --gold: #b8923e;
    --gold-light: #d9b865;
    --contact: #9fb2e0;
    --address: #c5cbe0;
    --ink: #1e2a4a;
    --ink-soft: #222;
  }
  * { margin: 0; padding: 0; box-sizing: border-box; }
  html, body { width: 1200px; height: 900px; overflow: hidden; }
  body {
    background: var(--page);
    font-family: "Roboto", sans-serif;
    position: relative;
  }
  .card {
    position: absolute;
    left: 100px; top: 166px;
    width: 1000px; height: 567px;
    border-radius: 28px;
    overflow: hidden;
    background: linear-gradient(180deg, var(--frost-top), var(--frost-bottom));
    box-shadow: 0 10px 30px rgba(30, 40, 70, 0.18);
  }
  .card-art { position: absolute; inset: 0; width: 1000px; height: 567px; }
  .brand-name {
    position: absolute;
    left: 68px; top: 255px;
    font-size: 60px;
    font-weight: 500;
    letter-spacing: 1px;
    color: var(--gold);
  }
  .brand-dot {
    position: absolute;
    left: 185px; top: 60px;
    width: 150px; height: 150px;
    border-radius: 50%;
    background: var(--navy);
  }
  .holder {
    position: absolute;
    right: 44px; top: 88px;
    text-align: right;
  }
  .holder-name { font-size: 38px; font-weight: 700; color: var(--ink); line-height: 1.1; }
  .holder-role { font-size: 25px; font-weight: 400; color: var(--ink-soft); margin-top: 10px; }
  .accent-bar {
    position: absolute;
    right: 0; top: 90px;
    width: 20px; height: 72px;
    background: var(--navy);
  }
  .contact {
    position: absolute;
    right: 44px; top: 328px;
    list-style: none;
    text-align: right;
  }
  .contact li {
    display: flex; justify-content: flex-end; align-items: center;
    font-size: 25px; color: var(--contact);
    height: 40px;
  }
  .contact svg { width: 24px; height: 24px; margin-left: 18px; }
  .address {
    position: absolute;
    right: 44px; top: 452px;
    text-align: right;
    font-size: 24px;
    line-height: 39px;
    color: var(--address);
  }
</style>
</head>
<body>
  <div class="card">
    <svg class="card-art" viewBox="0 0 1000 567" aria-hidden="true">
      <path d="M0,305 C130,430 320,470 520,390 C700,318 850,268 1000,272 L1000,567 L0,567 Z" fill="var(--navy)"/>
      <path d="M0,298 C130,420 320,460 520,380 C700,308 850,258 1000,266" fill="none" stroke="#ffffff" stroke-width="5" opacity="0.8"/>
      <path d="M0,280 C140,395 330,435 520,355 C700,282 860,222 985,258 C860,240 700,298 520,378 C320,462 120,432 0,312 Z" fill="var(--gold)"/>
    </svg>

    <div class="brand-dot"></div>
    <div class="brand-name">Mendwell47</div>

    <div class="holder">
      <div class="holder-name">Daniel Harper</div>
      <div class="holder-role">Owner</div>
    </div>
    <div class="accent-bar"></div>

    <ul class="contact">
      <li>123.456.7890
        <svg viewBox="0 0 24 24"><path d="M6.6 10.8a15 15 0 0 0 6.6 6.6l2.2-2.2a1 1 0 0 1 1-.25 11.4 11.4 0 0 0 3.6.57 1 1 0 0 1 1 1V20a1 1 0 0 1-1 1A17 17 0 0 1 3 4a1 1 0 0 1 1-1h3.5a1 1 0 0 1 1 1c0 1.25.2 2.45.57 3.57a1 1 0 0 1-.25 1Z" fill="var(--gold-light)"/></svg>
      </li>
      <li>info@webname.com
        <svg viewBox="0 0 24 24"><rect x="2" y="5" width="20" height="14" rx="1.5" fill="var(--gold)"/><path d="M2.5 6l9.5 7 9.5-7" fill="none" stroke="var(--navy)" stroke-width="1.8"/></svg>
      </li>
      <li>www.website.com
        <svg viewBox="0 0 24 24"><circle cx="12" cy="12" r="10" fill="var(--gold)"/><path d="M7 6c2 1 3 3 2 5s1 3 3 3-1 4 0 6M14 3c0 2 2 3 4 3s2 3 0 4" fill="none" stroke="var(--navy)" stroke-width="1.6"/></svg>
      </li>
    </ul>

    <div class="address">
      421, Address line goes here<br>
      45452, Country name
    </div>
  </div>
</body>
</html>
```